Email Signature

We are looking for creative email signature for our company. Please find attached the logo of our company for your reference. now we understand there isn't much can be done with email signature but we are looking for out of the box designs. Nothing specific in mind

Please insert fake numbers, website and/or address, etc just to showcase the designs. once the design is chosen we will provide the actual details.
Updates

Dear All,

We wouldlike to extend our apology for not being able to provide feedbacks to everysingle design. We were extremely busy and we have multiple contests opensimultaneously which makes the process harder. However, thank you all for theefforts you have put into this contest. We have received anoverwhelming quality responses & it has been a very difficult task tochoose just one, we easily Loved at least several designs...

Thanksagain for participating, we wish you all success in your design ventures.

Kindregards,

HLW Team

Industry/Entity Type

It Company

```html
<!DOCTYPE html>
<html lang="en">
<head>
<meta charset="utf-8">
<title>Email Signature – BrightQuay</title>
<link href="https://fonts.googleapis.com/css2?family=Arimo:wght@400;700&display=swap" rel="stylesheet">
<style>
  :root {
    --brand-blue: #4a93ee;
    --link-blue: #3e8be4;
    --accent-green: #7ed321;
    --ink: #2b2f33;
    --ink-soft: #222222;
    --paper: #ffffff;
  }
  html, body {
    margin: 0;
    padding: 0;
    overflow: hidden;
  }
  body {
    width: 1200px;
    height: 1000px;
    background: var(--paper);
    font-family: "Arimo", Arial, sans-serif;
    position: relative;
  }
  .signature {
    position: absolute;
    left: 0;
    top: 0;
    width: 1200px;
    height: 1000px;
  }
  .person-name {
    position: absolute;
    left: 176px;
    top: 422px;
    margin: 0;
    font-size: 20px;
    line-height: 24px;
    font-weight: 700;
    color: var(--ink);
  }
  .person-role {
    position: absolute;
    left: 176px;
    top: 449px;
    margin: 0;
    font-size: 13px;
    line-height: 16px;
    color: var(--ink);
  }
  .info-band {
    position: absolute;
    left: 157px;
    top: 474px;
    width: 633px;
    height: 47px;
    background: var(--brand-blue);
  }
  .social-icons {
    position: absolute;
    left: 173px;
    top: 489px;
    display: flex;
    gap: 12px;
    align-items: center;
  }
  .social-dot {
    width: 16px;
    height: 16px;
    border-radius: 50%;
    background: var(--paper);
  }
  .band-address {
    position: absolute;
    left: 434px;
    top: 494px;
    margin: 0;
    font-size: 12.5px;
    line-height: 15px;
    color: var(--paper);
  }
  .brand-name {
    position: absolute;
    left: 806px;
    top: 472px;
    margin: 0;
    font-size: 50px;
    line-height: 50px;
    font-weight: 700;
    color: var(--brand-blue);
    letter-spacing: -1px;
    white-space: nowrap;
  }
  .phone-row {
    position: absolute;
    left: 173px;
    top: 543px;
    margin: 0;
    font-size: 14px;
    line-height: 17px;
    color: var(--ink-soft);
    white-space: nowrap;
  }
  .phone-row .label {
    color: var(--accent-green);
    margin-right: 5px;
  }
  .phone-row .number {
    margin-right: 22px;
  }
  .email-link, .web-link {
    position: absolute;
    top: 575px;
    margin: 0;
    font-size: 14px;
    line-height: 17px;
    color: var(--link-blue);
  }
  .email-link { left: 176px; }
  .web-link { right: 167px; }
</style>
</head>
<body>
  <div class="signature">
    <h1 class="person-name">Mara Ellison</h1>
    <p class="person-role">Occupation</p>

    <div class="info-band"></div>
    <div class="social-icons">
      <span class="social-dot"></span>
      <span class="social-dot"></span>
      <svg class="mail-icon" width="22" height="16" viewBox="0 0 22 16" aria-label="Email">
        <rect x="1" y="1" width="20" height="14" fill="none" stroke="#ffffff" stroke-width="1.6"/>
        <polyline points="1,1 11,9 21,1" fill="none" stroke="#ffffff" stroke-width="1.6"/>
      </svg>
    </div>
    <p class="band-address">418 West Harbor Rd P.O. Box 3127 Calder,&nbsp; USA 41602</p>

    <p class="brand-name">BrightQuay</p>

    <p class="phone-row">
      <span class="label">Tel.:</span><span class="number">555-013-4470</span><span class="label">Fax:</span><span class="number">555-013-4471</span><span class="label">Mobile:</span><span class="number">555-013-4472</span>
    </p>

    <p class="email-link">hello@brightquay.com</p>
    <p class="web-link">www.brightquay.com</p>
  </div>
</body>
</html>
```